Business Card Design needed for logo design project

Would like a professional business card for a company involved in financial and latest technologies including CAD design. We would like the card to convey professionalism and communicate that we are involved in up to date technology solutions.

Target Market(s)

Business 2 Business sales

Industry/Entity Type

Financial

Colors

Designer to choose colors to be used in the design.

Requirements
Must have
• Business Name
Logo
Name
Phone
Email
Nice to have
• Website

```html
<!DOCTYPE html>
<html lang="en">
<head>
<meta charset="UTF-8">
<title>Vantrex Business Card</title>
<link rel="stylesheet" href="https://fonts.googleapis.com/css2?family=Poppins:wght@400;500;800&display=swap">
<style>
  :root {
    --backdrop: #8a8a8c;
    --navy: #141a2e;
    --navy-deep: #0c1122;
    --navy-soft: #1d2540;
    --red: #d6232b;
    --white: #ffffff;
    --ink: #1b2140;
    --muted-stripe: #ece6e6;
    --muted-stripe-2: #e3e4ea;
  }
  * { box-sizing: border-box; margin: 0; padding: 0; }
  html, body { width: 1200px; height: 900px; overflow: hidden; }
  body {
    background: var(--backdrop);
    font-family: "Poppins", sans-serif;
    position: relative;
  }
  .card {
    position: absolute;
    top: 300px;
    width: 520px;
    height: 300px;
    border-radius: 24px;
    overflow: hidden;
  }
  .card--back {
    left: 50px;
    background: linear-gradient(135deg, var(--navy-soft) 0%, var(--navy) 45%, var(--navy-deep) 100%);
  }
  .card--front { left: 630px; background: var(--navy); }

  .card__shade { position: absolute; inset: 0; width: 100%; height: 100%; }

  .wordmark {
    position: absolute;
    font-weight: 800;
    letter-spacing: 2px;
    line-height: 1;
  }
  .card--back .wordmark {
    left: 0; right: 0; top: 50%;
    transform: translateY(-50%);
    text-align: center;
    font-size: 58px;
    color: var(--white);
  }

  .front__top {
    position: absolute;
    left: 0; top: 0;
    width: 100%; height: 162px;
    background: var(--white);
  }
  .front__rule {
    position: absolute;
    left: 0; top: 162px;
    width: 100%; height: 7px;
    background: var(--red);
  }
  .card--front .wordmark {
    left: 0; right: 0; top: 72px;
    text-align: center;
    font-size: 52px;
    color: var(--red);
  }

  .holder {
    position: absolute;
    right: 290px; top: 212px;
    text-align: right;
  }
  .holder__name { color: var(--red); font-size: 20px; font-weight: 500; line-height: 1.2; }
  .holder__role { color: var(--white); font-size: 13px; line-height: 1.4; }

  .divider {
    position: absolute;
    left: 250px; top: 192px;
    width: 1px; height: 92px;
    background: var(--white);
    opacity: 0.7;
  }

  .contact {
    position: absolute;
    left: 264px; top: 192px;
    list-style: none;
    color: var(--white);
    font-size: 13px;
    line-height: 19px;
  }
  .contact li { display: flex; align-items: flex-start; gap: 6px; }
  .contact svg { width: 14px; height: 14px; margin-top: 2px; flex: none; fill: var(--red); }
</style>
</head>
<body>

<section class="card card--back" aria-label="Card back">
  <svg class="card__shade" viewBox="0 0 520 300" aria-hidden="true">
    <polygon points="300,0 520,0 520,110" fill="#ffffff" opacity="0.04"/>
    <polygon points="340,300 520,140 520,300" fill="#000000" opacity="0.18"/>
  </svg>
  <div class="wordmark">VANTREX</div>
</section>

<section class="card card--front" aria-label="Card front">
  <div class="front__top">
    <svg class="card__shade" viewBox="0 0 520 162" aria-hidden="true">
      <polygon points="350,22 480,22 430,150" fill="var(--muted-stripe)"/>
      <polygon points="470,22 520,22 520,150 490,150" fill="var(--muted-stripe-2)"/>
    </svg>
  </div>
  <div class="front__rule"></div>
  <div class="wordmark">VANTREX</div>

  <div class="holder">
    <p class="holder__name">Milo Grant Avery</p>
    <p class="holder__role">Manager</p>
  </div>

  <div class="divider"></div>

  <ul class="contact">
    <li>
      <svg viewBox="0 0 24 24" aria-hidden="true"><path d="M6.6 10.8a15.1 15.1 0 0 0 6.6 6.6l2.2-2.2c.3-.3.7-.4 1-.2 1.1.4 2.3.6 3.6.6.6 0 1 .4 1 1V20c0 .6-.4 1-1 1A17 17 0 0 1 3 4c0-.6.4-1 1-1h3.5c.6 0 1 .4 1 1 0 1.3.2 2.5.6 3.6.1.3 0 .7-.2 1z"/></svg>
      <span>555-214-6078</span>
    </li>
    <li>
      <svg viewBox="0 0 24 24" aria-hidden="true"><path d="M3 5h18c.6 0 1 .4 1 1v12c0 .6-.4 1-1 1H3c-.6 0-1-.4-1-1V6c0-.6.4-1 1-1zm1 2.3V17h16V7.3l-8 5.2z M4.8 7h14.4L12 11.6z"/></svg>
      <span>hello@vantrex.com</span>
    </li>
    <li>
      <svg viewBox="0 0 24 24" aria-hidden="true"><path d="M12 2a10 10 0 1 0 0 20 10 10 0 0 0 0-20zm6.9 9h-3a15 15 0 0 0-1.3-6.1A8 8 0 0 1 18.9 11zM12 4c.9 1.2 1.8 3.7 1.9 7h-3.8c.1-3.3 1-5.8 1.9-7zM9.4 4.9A15 15 0 0 0 8.1 11h-3a8 8 0 0 1 4.3-6.1zM5.1 13h3a15 15 0 0 0 1.3 6.1A8 8 0 0 1 5.1 13zM12 20c-.9-1.2-1.8-3.7-1.9-7h3.8c-.1 3.3-1 5.8-1.9 7zm2.6-.9a15 15 0 0 0 1.3-6.1h3a8 8 0 0 1-4.3 6.1z"/></svg>
      <span>www.vantrex.com</span>
    </li>
    <li>
      <svg viewBox="0 0 24 24" aria-hidden="true"><path d="M12 3l10 9h-3v9h-5v-6h-4v6H5v-9H2z"/></svg>
      <span>4820 N. Harlow Parkway,<br>Austin, Texas 73301</span>
    </li>
  </ul>
</section>

</body>
</html>
```